Presentation Folder Design - (Pocket Folder)

We are an accounting firm for dentists. We need a folder designed for our marketing material. Attached is our logo.

Industry/Entity Type

Accounting

```html
<!DOCTYPE html>
<html lang="en">
<head>
<meta charset="utf-8">
<title>Molarline Dental CPAs – Presentation Folder</title>
<link rel="stylesheet" href="https://fonts.googleapis.com/css2?family=Montserrat:wght@700&family=Open+Sans:wght@400&display=swap">
<style>
  :root {
    --stage: #d9dadc;
    --paper: #fbfbfd;
    --paper-shade: #eef0f5;
    --brand-blue: #1f9ad6;
    --deep-blue: #2a4f9e;
    --violet: #7c76b8;
    --ink-grey: #6b6d72;
    --fold-line: #d3d6de;
  }
  * { box-sizing: border-box; margin: 0; padding: 0; }
  html, body {
    width: 1200px; height: 847px; overflow: hidden;
    background: var(--stage);
  }
  .folder-spread {
    position: absolute; left: 150px; top: 103px;
    width: 900px; height: 640px;
    display: flex;
    box-shadow: 0 10px 30px rgba(0,0,0,.18);
  }
  .panel {
    position: relative; width: 450px; height: 640px;
    background: linear-gradient(160deg, var(--paper) 40%, var(--paper-shade));
    overflow: hidden;
  }
  .panel--back { border-right: 1px solid var(--fold-line); }
  .wave-art { position: absolute; inset: 0; width: 100%; height: 100%; }
  .wordmark {
    position: absolute;
    font-family: "Montserrat", sans-serif; font-weight: 700;
    color: var(--brand-blue); line-height: 1.05; letter-spacing: -0.5px;
  }
  .wordmark--front { top: 60px; left: 0; right: 0; text-align: center; font-size: 34px; }
  .wordmark--back { left: 40px; top: 462px; font-size: 22px; }
  .contact-list {
    position: absolute; left: 40px; top: 530px; list-style: none;
    font-family: "Open Sans", sans-serif; font-size: 10px;
    letter-spacing: 1px; color: var(--ink-grey);
  }
  .contact-list li { display: flex; align-items: center; gap: 9px; height: 17px; }
  .contact-icon { width: 10px; height: 10px; flex: none; }
</style>
</head>
<body>
  <main class="folder-spread">
    <section class="panel panel--back" aria-label="Back cover">
      <svg class="wave-art" viewBox="0 0 450 640" role="img" aria-label="Abstract blue and violet light swoosh along the left edge">
        <defs>
          <linearGradient id="backSweep" x1="0" y1="0" x2="1" y2="0">
            <stop offset="0" stop-color="#2a4f9e"/>
            <stop offset=".35" stop-color="#5b7cc4" stop-opacity=".7"/>
            <stop offset="1" stop-color="#ffffff" stop-opacity="0"/>
          </linearGradient>
          <linearGradient id="backTop" x1="0" y1="0" x2="0" y2="1">
            <stop offset="0" stop-color="#7c76b8" stop-opacity=".55"/>
            <stop offset="1" stop-color="#ffffff" stop-opacity="0"/>
          </linearGradient>
        </defs>
        <rect x="0" y="0" width="450" height="60" fill="url(#backTop)"/>
        <path d="M0 20 C 90 120, 140 260, 60 420 L0 440 Z" fill="url(#backSweep)"/>
      </svg>
      <div class="wordmark wordmark--back">Molarline<br>Dental CPAs</div>
      <ul class="contact-list">
        <li><svg class="contact-icon" viewBox="0 0 10 10"><path d="M2 1h2l1 2-1 1c.6 1.2 1.4 2 2.6 2.6l1-1 2 1v2c-4 .5-8-3.5-7.6-7.6z" fill="#2a4f9e"/></svg>(555) 014-2290</li>
        <li><svg class="contact-icon" viewBox="0 0 10 10"><rect x="1" y="3" width="8" height="5" fill="#2a4f9e"/><rect x="3" y="1" width="4" height="2" fill="#2a4f9e"/></svg>(555) 014-2291 fax</li>
        <li><svg class="contact-icon" viewBox="0 0 10 10"><rect x="1" y="2" width="8" height="6" fill="#2a4f9e"/><path d="M1 2l4 3 4-3" stroke="#fff" fill="none"/></svg>office@molarlinecpas.com</li>
        <li><svg class="contact-icon" viewBox="0 0 10 10"><circle cx="5" cy="5" r="4" fill="none" stroke="#2a4f9e" stroke-width="1.4"/><path d="M1 5h8M5 1v8" stroke="#2a4f9e"/></svg>www.molarlinecpas.com</li>
      </ul>
    </section>
    <section class="panel panel--front" aria-label="Front cover">
      <svg class="wave-art" viewBox="0 0 450 640" role="img" aria-label="Abstract blue and violet light swoosh across the lower cover">
        <defs>
          <linearGradient id="frontBand" x1="0" y1="0" x2="1" y2="1">
            <stop offset="0" stop-color="#ffffff" stop-opacity="0"/>
            <stop offset=".5" stop-color="#7c76b8" stop-opacity=".6"/>
            <stop offset="1" stop-color="#2a4f9e"/>
          </linearGradient>
          <linearGradient id="frontEdge" x1="1" y1="0" x2="0" y2="0">
            <stop offset="0" stop-color="#1f6fc0" stop-opacity=".8"/>
            <stop offset="1" stop-color="#ffffff" stop-opacity="0"/>
          </linearGradient>
        </defs>
        <rect x="0" y="0" width="450" height="14" fill="#c8cde4"/>
        <path d="M450 150 C 400 200, 330 250, 250 300 L450 330 Z" fill="url(#frontEdge)"/>
        <path d="M0 520 C 150 490, 320 450, 450 400 L450 640 L0 640 Z" fill="url(#frontBand)"/>
        <path d="M0 520 C 150 490, 320 450, 450 400" stroke="#2a4f9e" stroke-width="2" fill="none"/>
      </svg>
      <div class="wordmark wordmark--front">Molarline<br>Dental CPAs</div>
    </section>
  </main>
</body>
</html>
```